Website Landing Page for Brightfall Systems

Create a custom designed website landing page for our business. Looking for a professional upscale design that incorporates our logo and logo colors into the theme. I want a standard fixed frame website, not a constant scrolling format that seems to be the trend. To start with I'm looking for more of the graphic design part, maybe a concept or theme, I don't expect to see a finished project. Not interested in generic templates or layouts.

The name of our company is Brightfall Systems and I've attached our logo below. I'd like to have the web page have the same look and feel of our logo, as well as the colors. Our company, Brightfall Systems does system design, installation, and programming, of residential and commercial Audio/Video and Automation systems. We do home theaters, lighting and building automation, video conferencing systems, security camera installations, conference rooms, projectors, distributed audio systems, and similar Technology projects. This will be a professional services/informational website. We will not sell products on this website. This website will be used to advertise our company and communicate our services to prospective customers. Having a well designed, professional and clean website is one way we want to distinguish our company from the competition.

Here are some examples of what I consider a professional well designed website
http://www.qorlamstudio.com/Work/

Last year we had our tradlo store designed (with PixelMarket) and I'm really happy with the way it turned out. You can see it at www.HolvenGearDepot.com I consider this to be a great design and looking for the same level of quality with this new website. However, do not copy or use any part of this design in this new project. This tradlo store is completely separate from our other company Brightfall Systems. I only mention this tradlo store an an example of good work.

Reason: Still going through designs.

Reason: Still working on project and have not had time to review all designs and request revisions.

Reason: Sill going through designs and requesting revisions

Reason: still going through all the submissions we received.

Target Market(s)

People interested in Audio/Video, home theaters, home automation. We do sales, system design, and programming. We typically work on larger projects with both residential and commercial customers.

Industry/Entity Type

Business

Number of Pages Required

1 page

Requirements
Must have
• Great design elements. Please use a white background. I think white goes well with our logo colors.

```html
<!DOCTYPE html>
<html lang="en">
<head>
<meta charset="utf-8">
<title>Brightfall Systems</title>
<link href="https://fonts.googleapis.com/css2?family=Bebas+Neue&family=Montserrat:wght@400;500;600;700&display=swap" rel="stylesheet">
<style>
  :root {
    --blue: #3a8fd3;
    --blue-dark: #2a78bf;
    --green: #7dc242;
    --green-dark: #5fae2c;
    --text: #555a60;
    --white: #ffffff;
  }
  * { margin: 0; padding: 0; box-sizing: border-box; }
  html, body { width: 1200px; height: 1053px; overflow: hidden; background: var(--white); }
  body { font-family: "Montserrat", Arial, sans-serif; color: var(--text); position: relative; }

  .brand { position: absolute; left: 61px; top: 205px; width: 290px; text-align: center; }
  .brand-name { font-family: "Bebas Neue", "Arial Narrow", sans-serif; font-weight: 400; font-size: 56px; line-height: 56px; color: var(--blue); letter-spacing: 1px; }

  .section-title { position: absolute; left: 61px; font-size: 12px; font-weight: 700; color: var(--blue); letter-spacing: .3px; }
  .about-text { position: absolute; left: 61px; top: 377px; width: 318px; font-size: 10.4px; line-height: 15px; }

  .service { position: absolute; width: 100px; font-size: 10px; line-height: 11px; color: #333; }
  .service svg { display: block; width: 38px; height: 34px; margin-bottom: 10px; }

  .testimonial { position: absolute; left: 61px; width: 306px; font-size: 10.6px; line-height: 15px; }
  .testimonial p { padding-left: 12px; }
  .testimonial cite { display: block; text-align: right; font-style: normal; font-size: 8px; color: var(--blue); margin-top: 4px; }

  .social { position: absolute; top: 978px; left: 63px; display: flex; gap: 16px; }
  .social-tile { width: 48px; height: 48px; border-radius: 6px; display: flex; align-items: center; justify-content: center; font-size: 8px; font-weight: 600; color: var(--white); }
  .tile-green { background: linear-gradient(180deg, #8ad04e, var(--green-dark)); }
  .tile-blue { background: linear-gradient(180deg, #4aa3e6, var(--blue-dark)); }

  .project { position: absolute; width: 362px; overflow: hidden; }
  .project-photo { position: absolute; inset: 0; }
  .caption { position: absolute; right: 4px; bottom: 5px; width: 212px; height: 67px; padding: 12px 12px 0 12px; color: var(--white); }
  .caption::before, .caption::after { content: ""; position: absolute; width: 22px; height: 14px; border-color: var(--white); border-style: solid; }
  .caption::before { left: 5px; top: 5px; border-width: 1px 0 0 1px; }
  .caption::after { right: 5px; bottom: 5px; border-width: 0 1px 1px 0; }
  .caption-blue { background: var(--blue); }
  .caption-green { background: var(--green); }
  .caption h3 { font-family: "Bebas Neue", "Arial Narrow", sans-serif; font-weight: 400; font-size: 15px; letter-spacing: .3px; margin-bottom: 5px; }
  .caption p { font-size: 7px; line-height: 10px; }
</style>
</head>
<body>

  <header class="brand">
    <div class="brand-name">BRIGHTFALL<br>SYSTEMS</div>
  </header>

  <h2 class="section-title" style="top:355px">WHO ARE WE</h2>
  <p class="about-text">Lorem ipsum dolor sit amet, consectetur adipiscing elit. Quisque elementum nunc nec leo eleifend vulputate. Nam interdum lacus mauris, a euismod metus molestie eget. Donec mattis, diam quis varius laoreet, est ante commodo odio, non suscipit sem nunc vitae nisi.</p>

  <h2 class="section-title" style="top:484px">WHAT WE DO</h2>

  <div class="service" style="left:61px;top:522px">
    <svg viewBox="0 0 38 34"><rect x="3" y="6" width="26" height="11" rx="2" transform="rotate(18 16 11)" fill="var(--blue)"/><rect x="24" y="20" width="4" height="10" fill="var(--blue)"/><rect x="22" y="28" width="12" height="3" fill="var(--blue)"/></svg>
    Security<br>Systems
  </div>
  <div class="service" style="left:164px;top:522px">
    <svg viewBox="0 0 38 34"><circle cx="17" cy="13" r="9" fill="none" stroke="var(--green)" stroke-width="2.5"/><rect x="13" y="23" width="8" height="7" rx="1" fill="var(--green)"/><circle cx="30" cy="8" r="4" fill="none" stroke="var(--green)" stroke-width="2"/></svg>
    Lighting<br>Automation
  </div>
  <div class="service" style="left:273px;top:522px">
    <svg viewBox="0 0 38 34"><rect x="3" y="9" width="32" height="17" rx="4" fill="var(--blue)"/><circle cx="13" cy="17.5" r="5" fill="var(--white)"/><circle cx="13" cy="17.5" r="2.5" fill="var(--blue)"/><rect x="22" y="14" width="9" height="2" fill="var(--white)"/><rect x="22" y="19" width="9" height="2" fill="var(--white)"/></svg>
    Video System<br>Setup
  </div>
  <div class="service" style="left:61px;top:631px">
    <svg viewBox="0 0 38 34"><rect x="5" y="2" width="28" height="18" rx="2" fill="var(--green)"/><rect x="9" y="6" width="20" height="10" fill="var(--white)"/><rect x="4" y="25" width="30" height="7" rx="3" fill="var(--green)"/></svg>
    Conference<br>Systems
  </div>
  <div class="service" style="left:164px;top:631px">
    <svg viewBox="0 0 38 34"><path d="M6 12 L14 12 L24 4 L24 30 L14 22 L6 22 Z" fill="var(--blue)"/><path d="M28 11 Q32 17 28 23" fill="none" stroke="var(--blue)" stroke-width="2.5"/></svg>
    Audio<br>Systems
  </div>
  <div class="service" style="left:273px;top:631px">
    <svg viewBox="0 0 38 34"><circle cx="17" cy="17" r="11" fill="none" stroke="var(--green)" stroke-width="6" stroke-dasharray="5 3.6"/><circle cx="17" cy="17" r="7" fill="var(--green)"/><circle cx="17" cy="17" r="3" fill="var(--white)"/></svg>
    <span style="position:relative;top:-10px">More Services</span>
  </div>

  <h2 class="section-title" style="top:738px">OUR CLIENTS SAY</h2>
  <blockquote class="testimonial" style="top:761px"><p>“Lorem ipsum dolor sit amet, consectetur adipiscing elit. Quisque elementum nunc nec leo vulputate.”</p><cite>Aaron Pell | Corvane Works</cite></blockquote>
  <blockquote class="testimonial" style="top:828px"><p>“Lorem ipsum dolor sit amet, consectetur adipiscing elit. Quisque elementum nunc nec leo vulputate.”</p><cite>Lena Marsh | Residential Fit Out</cite></blockquote>
  <blockquote class="testimonial" style="top:895px"><p>“Lorem ipsum dolor sit amet, consectetur adipiscing elit. Quisque elementum nunc nec leo vulputate.”</p><cite>Owen Tate | Hotel on Averly Park</cite></blockquote>

  <nav class="social">
    <div class="social-tile tile-green">Chatwave</div>
    <div class="social-tile tile-blue">Friendly</div>
    <div class="social-tile tile-green">Pictora</div>
    <div class="social-tile tile-blue">Callnest</div>
    <div class="social-tile tile-green"><svg width="34" height="24" viewBox="0 0 34 24"><rect x="1.5" y="1.5" width="31" height="21" fill="none" stroke="var(--white)" stroke-width="2.5"/><path d="M2 2 L17 14 L32 2" fill="none" stroke="var(--white)" stroke-width="2.5"/></svg></div>
  </nav>

  <article class="project" style="left:439px;top:0;height:341px">
    <div class="project-photo" role="img" aria-label="Large auditorium with tiered dark seating and a stage" style="background:linear-gradient(160deg,#c9c8c4,#8d8f93 55%,#4c5058)"></div>
    <div class="caption caption-blue"><h3>LARGE SCALE PROJECTS...</h3><p>Lorem ipsum dolor sit amet, consectetur adipiscing elit. Quisque elementum nunc nec leo eleifend.</p></div>
  </article>
  <article class="project" style="left:822px;top:0;height:341px">
    <div class="project-photo" role="img" aria-label="Lit villa entrance with palm trees at dusk" style="background:linear-gradient(180deg,#1c4fb8,#4d6d9a 40%,#b98e55 70%,#4f5a2e)"></div>
    <div class="caption caption-green"><h3>RESIDENTIAL PROJECTS...</h3><p>Lorem ipsum dolor sit amet, consectetur adipiscing elit. Quisque elementum nunc nec leo eleifend.</p></div>
  </article>
  <article class="project" style="left:439px;top:365px;height:373px">
    <div class="project-photo" role="img" aria-label="Living room with sectional sofa, ceiling projector and large wall screen" style="background:linear-gradient(170deg,#e6dfd2,#c9b89b 50%,#7d6a55)"></div>
    <div class="caption caption-green"><h3>AUDIO &amp; VISUAL PROJECTS...</h3><p>Lorem ipsum dolor sit amet, consectetur adipiscing elit. Quisque elementum nunc nec leo eleifend.</p></div>
  </article>
  <article class="project" style="left:822px;top:365px;height:373px">
    <div class="project-photo" role="img" aria-label="Restaurant bar with glass wine tower and stools on a wooden floor" style="background:linear-gradient(175deg,#5a5e63,#3b3a38 50%,#8a4f2c)"></div>
    <div class="caption caption-blue"><h3>COMMERCIAL PROJECTS...</h3><p>Lorem ipsum dolor sit amet, consectetur adipiscing elit. Quisque elementum nunc nec leo eleifend.</p></div>
  </article>
  <article class="project" style="left:439px;top:761px;height:292px">
    <div class="project-photo" role="img" aria-label="Conference room with wall-mounted display, wood panelling and meeting table" style="background:linear-gradient(180deg,#e8e8e8,#7b5a48 45%,#3d2f29)"></div>
    <div class="caption caption-blue"><h3>CONFERENCE PROJECTS...</h3><p>Lorem ipsum dolor sit amet, consectetur adipiscing elit. Quisque elementum nunc nec leo eleifend.</p></div>
  </article>
  <article class="project" style="left:822px;top:761px;height:292px">
    <div class="project-photo" role="img" aria-label="Ornate hotel lobby with columns and chandeliers" style="background:linear-gradient(170deg,#c9a462,#a67a3b 50%,#6b4a22)"></div>
    <div class="caption caption-green"><h3>HOTEL PROJECTS...</h3><p>Lorem ipsum dolor sit amet, consectetur adipiscing elit. Quisque elementum nunc nec leo eleifend.</p></div>
  </article>

</body>
</html>
```